Harlow Company Core Values

We are looking for an updated appearance to our Core Values with the addition of some descriptors to share with new hires, employees, and potential candidates

Requirements
Must have
• Core values and core value descriptors

```html
<!DOCTYPE html>
<html lang="en">
<head>
<meta charset="utf-8">
<title>Harlow Company — Core Values</title>
<link href="https://fonts.googleapis.com/css2?family=Montserrat:wght@600;700;800&family=Open+Sans:ital,wght@0,400;0,600;1,600&display=swap" rel="stylesheet">
<style>
  :root {
    --red: #ad1e2d;
    --red-dark: #8e1522;
    --black: #1f1d1e;
    --grey-bg: #d4d4d4;
    --white: #ffffff;
    --ink: #2a2a2a;
  }
  * { margin: 0; padding: 0; box-sizing: border-box; }
  html, body {
    width: 1200px; height: 1200px; overflow: hidden;
    background: var(--grey-bg);
  }
  .sheet {
    position: absolute; left: 150px; top: 18px;
    width: 900px; height: 1164px;
    background: var(--white);
    box-shadow: 0 6px 24px rgba(0,0,0,0.15);
    overflow: hidden;
  }
  .brand {
    position: absolute; left: 60px; top: 52px;
    display: flex; align-items: center; gap: 14px;
  }
  .brand-dot {
    width: 54px; height: 54px; border-radius: 50%;
    background: var(--red);
  }
  .brand-name {
    font-family: "Open Sans", sans-serif; font-weight: 400;
    font-size: 38px; color: var(--ink); letter-spacing: 0.5px;
  }
  .tagline {
    position: absolute; left: 130px; top: 112px;
    font-family: "Open Sans", sans-serif; font-style: italic; font-weight: 600;
    font-size: 14px; color: var(--red);
  }
  .title {
    position: absolute; right: 40px; top: 210px;
    display: flex; align-items: stretch; gap: 10px;
  }
  .title-text {
    font-family: "Montserrat", sans-serif; font-weight: 800;
    font-size: 38px; line-height: 0.95; text-align: right; color: var(--black);
  }
  .title-bar { width: 12px; background: var(--red); }
  .wheel {
    position: absolute; left: 90px; top: 300px;
    width: 720px; height: 720px;
  }
  .seg-red { fill: var(--red); }
  .seg-black { fill: var(--black); }
  .badge-red { fill: var(--white); stroke: var(--red); stroke-width: 8; }
  .badge-black { fill: var(--white); stroke: var(--black); stroke-width: 8; }
  .badge-num {
    font-family: "Montserrat", sans-serif; font-weight: 800; font-size: 22px;
    fill: var(--black); text-anchor: middle; dominant-baseline: central;
  }
  .value-name {
    font-family: "Montserrat", sans-serif; font-weight: 700; font-size: 19px;
    fill: var(--white); text-anchor: middle;
  }
  .value-desc {
    font-family: "Open Sans", sans-serif; font-size: 12px;
    fill: var(--white); text-anchor: middle;
  }
  .hub-num {
    font-family: "Montserrat", sans-serif; font-weight: 800; font-size: 32px;
    fill: var(--white); text-anchor: middle;
  }
  .footer {
    position: absolute; left: 0; bottom: 0; width: 100%; height: 46px;
    background: var(--red);
    display: flex; align-items: center; justify-content: center;
    font-family: "Open Sans", sans-serif; font-size: 14px; color: var(--white);
    letter-spacing: 0.2px;
  }
</style>
</head>
<body>
  <main class="sheet">
    <header>
      <div class="brand">
        <span class="brand-dot"></span>
        <span class="brand-name">Harlow Company</span>
      </div>
      <p class="tagline">Keeping Things in Motion · Since 1868</p>
      <h1 class="title">
        <span class="title-text">CORE<br>VALUES</span>
        <span class="title-bar"></span>
      </h1>
    </header>

    <svg class="wheel" viewBox="-360 -360 720 720" aria-label="Core values wheel">
      <g class="segments">
        <path class="seg-red" d="M-149.8,-294 A330,330 0 0 1 149.8,-294 L68.1,-133.7 A150,150 0 0 0 -68.1,-133.7 Z"/>
        <path class="seg-black" d="M179.7,-276.8 A330,330 0 0 1 329.5,-17.3 L149.8,-7.9 A150,150 0 0 0 81.7,-125.8 Z"/>
        <path class="seg-red" d="M329.5,17.3 A330,330 0 0 1 179.7,276.8 L81.7,125.8 A150,150 0 0 0 149.8,7.9 Z"/>
        <path class="seg-black" d="M149.8,294 A330,330 0 0 1 -149.8,294 L-68.1,133.7 A150,150 0 0 0 68.1,133.7 Z"/>
        <path class="seg-red" d="M-179.7,276.8 A330,330 0 0 1 -329.5,17.3 L-149.8,7.9 A150,150 0 0 0 -81.7,125.8 Z"/>
        <path class="seg-black" d="M-329.5,-17.3 A330,330 0 0 1 -179.7,-276.8 L-81.7,-125.8 A150,150 0 0 0 -149.8,-7.9 Z"/>
      </g>

      <g class="hub">
        <circle r="108" class="seg-red"/>
        <text class="hub-num" y="-28">06</text>
        <text class="value-name" y="2">Work Smart</text>
        <text class="value-desc" y="26">Plan ahead, focus,</text>
        <text class="value-desc" y="42">seek to understand</text>
      </g>

      <g class="badges">
        <circle class="badge-red" cx="0" cy="-150" r="28"/><text class="badge-num" x="0" y="-150">01</text>
        <circle class="badge-black" cx="130" cy="-75" r="28"/><text class="badge-num" x="130" y="-75">02</text>
        <circle class="badge-red" cx="130" cy="75" r="28"/><text class="badge-num" x="130" y="75">03</text>
        <circle class="badge-black" cx="0" cy="150" r="28"/><text class="badge-num" x="0" y="150">04</text>
        <circle class="badge-red" cx="-130" cy="75" r="28"/><text class="badge-num" x="-130" y="75">05</text>
        <circle class="badge-black" cx="-130" cy="-75" r="28"/><text class="badge-num" x="-130" y="-75">05</text>
      </g>

      <g class="values">
        <text class="value-name" x="0" y="-258">Respect Everyone</text>
        <text class="value-desc" x="0" y="-236">Listen first, value</text>
        <text class="value-desc" x="0" y="-220">every voice</text>

        <text class="value-name" x="200" y="-182">Aim for</text>
        <text class="value-name" x="200" y="-160">excellence</text>
        <text class="value-desc" x="205" y="-138">Learn from mistakes</text>
        <text class="value-desc" x="210" y="-122">and raise the bar</text>

        <text class="value-name" x="205" y="132">Take Care</text>
        <text class="value-desc" x="205" y="154">Of people, equipment</text>
        <text class="value-desc" x="205" y="170">and our shared home</text>

        <text class="value-name" x="0" y="218">Communicate</text>
        <text class="value-desc" x="0" y="240">Listen with intent and</text>
        <text class="value-desc" x="0" y="256">share ideas openly</text>

        <text class="value-name" x="-205" y="132">Act Ethically</text>
        <text class="value-desc" x="-205" y="154">Do the right thing</text>
        <text class="value-desc" x="-205" y="170">even when unseen</text>

        <text class="value-name" x="-200" y="-182">Share your</text>
        <text class="value-name" x="-200" y="-160">passion</text>
        <text class="value-desc" x="-205" y="-138">Bring energy and pride</text>
        <text class="value-desc" x="-210" y="-122">to the work we do</text>
      </g>
    </svg>

    <footer class="footer">
      1410 North Alder Road | Millbrook, California 90210 | Phone 555.014.2200 | Fax 555.014.2201 | 800.555.0168 | harlowco.example
    </footer>
  </main>
</body>
</html>
```